Brightway Dwelling & Yard Care - Maintenance & Improvements

Handyman service - Total home improvement and maintenance

We do everything indoors, ie. carpentry, and outdoors, ie. garden maintenance

No job too small or too unusual

7 Days per week
Updates

I want the overall impression not to favour either gender ... eg. maybe don't use the word Handy'man' because we also have a Fixmistress service .... but just stay with a generic theme of home improvement and maintenance

Industry/Entity Type

Home Improvement

Contact Information for Business Card

Brightway Dwelling & Yard Care
7 Days per Week
Total Home Maintenance and Improvements
Handyman | Fixmistress | Our (DIY) Task Pal
Ph: 0487 613 902
www.brightwaydwellingyard.com.au

Requirements
Must have
• The black and white image of various workers, as per attached

```html
<!DOCTYPE html>
<html lang="en">
<head>
<meta charset="utf-8">
<title>Brightway Dwelling &amp; Yard Care – Business Card</title>
<link href="https://fonts.googleapis.com/css2?family=Open+Sans:wght@400;600;700&display=swap" rel="stylesheet">
<style>
  :root {
    --stage: #2b2b2b;
    --card: #ffffff;
    --ink: #1c1c1c;
    --ink-soft: #333333;
    --workers: #e2e2e2;
    --garden-green: #3f7a3a;
    --garden-wood: #b9875a;
    --cushion-orange: #e0642a;
    --interior-red: #c23a2c;
    --frame-wood: #d9a36b;
  }
  * { margin: 0; padding: 0; box-sizing: border-box; }
  html, body { width: 1200px; height: 716px; overflow: hidden; }
  body {
    background: var(--stage);
    font-family: "Open Sans", Verdana, sans-serif;
    display: flex; align-items: center; justify-content: center;
  }
  .business-card {
    position: relative;
    width: 900px; height: 515px;
    background: var(--card);
    overflow: hidden;
    color: var(--ink);
  }
  .workers-band {
    position: absolute; left: 0; bottom: 0;
    width: 580px; height: 150px;
    background: linear-gradient(90deg, var(--workers) 0%, #efefef 55%, rgba(255,255,255,0) 100%);
    opacity: .7;
  }
  .photo-panel { position: absolute; inset: 0; width: 900px; height: 515px; }
  .card-text { position: absolute; left: 48px; top: 44px; width: 520px; }
  .brand-lead { font-weight: 700; font-size: 22px; line-height: 1.1; }
  .brand-name { font-weight: 400; font-size: 44px; line-height: 1.15; letter-spacing: .2px; }
  .tagline { margin-top: 10px; font-size: 19px; line-height: 1.3; color: var(--ink-soft); }
  .service-name { margin-top: 40px; font-weight: 700; font-size: 24px; line-height: 1.2; }
  .service-sub { font-size: 19px; color: var(--ink-soft); line-height: 1.3; }
  .contact-row { display: flex; align-items: center; gap: 10px; font-size: 19px; line-height: 1.45; color: var(--ink-soft); }
  .contact-row svg { width: 18px; height: 18px; flex: none; }
</style>
</head>
<body>
  <article class="business-card">
    <div class="workers-band" role="img" aria-label="Black and white silhouettes of various tradespeople at work"></div>

    <svg class="photo-panel" viewBox="0 0 900 515" role="img" aria-label="Photo collage: a garden pergola with outdoor lounge above, and people building a timber frame indoors below">
      <defs>
        <linearGradient id="garden" x1="0" y1="0" x2="0" y2="1">
          <stop offset="0" stop-color="var(--garden-green)"/>
          <stop offset=".55" stop-color="var(--garden-wood)"/>
          <stop offset="1" stop-color="var(--cushion-orange)"/>
        </linearGradient>
        <linearGradient id="interior" x1="0" y1="0" x2="1" y2="1">
          <stop offset="0" stop-color="var(--frame-wood)"/>
          <stop offset=".55" stop-color="var(--interior-red)"/>
          <stop offset="1" stop-color="#8c2a22"/>
        </linearGradient>
        <clipPath id="strip-shape">
          <path d="M730 0 H900 V515 H615 C600 445 605 385 645 320 C695 240 705 130 730 0 Z"/>
        </clipPath>
      </defs>
      <g clip-path="url(#strip-shape)">
        <rect x="560" y="0" width="340" height="515" fill="url(#garden)"/>
        <rect x="560" y="318" width="340" height="197" fill="url(#interior)"/>
        <line x1="560" y1="318" x2="900" y2="318" stroke="#ffffff" stroke-width="4"/>
      </g>
    </svg>

    <div class="card-text">
      <div class="brand-lead">Brightway</div>
      <div class="brand-name">Dwelling &amp; Yard Care</div>
      <p class="tagline">7 Days per Week Total Home Maintenance<br>Improvements Handyman</p>
      <div class="service-name">Fixmistress</div>
      <div class="service-sub">Our (DIY) Task Pal</div>
      <div class="contact-row">
        <svg viewBox="0 0 24 24" aria-hidden="true"><path fill="var(--ink)" d="M6.6 10.8a15 15 0 0 0 6.6 6.6l2.2-2.2c.3-.3.7-.4 1-.2 1.1.4 2.3.6 3.6.6.6 0 1 .4 1 1V20c0 .6-.4 1-1 1A17 17 0 0 1 3 4c0-.6.4-1 1-1h3.5c.6 0 1 .4 1 1 0 1.3.2 2.5.6 3.6.1.3 0 .7-.2 1z"/></svg>
        <span>0487 613 902</span>
      </div>
      <div class="contact-row">
        <svg viewBox="0 0 24 24" aria-hidden="true"><circle cx="12" cy="12" r="9.5" fill="none" stroke="var(--ink)" stroke-width="2"/><ellipse cx="12" cy="12" rx="4" ry="9.5" fill="none" stroke="var(--ink)" stroke-width="1.6"/><path d="M2.5 12h19" stroke="var(--ink)" stroke-width="1.6"/></svg>
        <span>www.brightwaydwellingyard.com.au</span>
      </div>
    </div>
  </article>
</body>
</html>
```